Banner Design for Physiotherapy Business

I need a banner designed for a physiotherapy business. The word ‘Physiotherapy’ should be prominent at the top. I’ve attached a document outlining what text and a suggestion of a picture I’d like included. The photo I have suggested in the document won’t upload to artvolley though as the dimensions are too large. I am open to other photos being used though. I would like to see designs that use the colour orange (as seen in the example) or green preferrably. The dimensions need to be 841mm x 2055mm and provided in PDF, JPG, and PNG format and 300dpi in CMYK colour mode.

```html
<!DOCTYPE html>
<html lang="en">
<head>
<meta charset="utf-8">
<title>Physiotherapy Roll-up Banner</title>
<link href="https://fonts.googleapis.com/css2?family=Montserrat:wght@800&family=Mulish:wght@400;600&family=Barlow+Semi+Condensed:wght@600&display=swap" rel="stylesheet">
<style>
  :root{
    --orange-light:#e8993c;
    --orange-dark:#e57133;
    --orange-text:#e8652a;
    --text-grey:#58595b;
    --navy:#1f2f5c;
    --badge-blue:#2a7fc9;
    --pale:#fdf1e4;
    --white:#ffffff;
    --backdrop:#ececec;
  }
  *{margin:0;padding:0;box-sizing:border-box}
  html,body{width:1200px;height:900px;overflow:hidden}
  body{background:var(--backdrop);position:relative;font-family:'Mulish',sans-serif}
  .banner{position:absolute;left:424px;top:20px;width:352px;height:860px;background:var(--white);overflow:hidden;box-shadow:0 4px 18px rgba(0,0,0,.12)}
  .title-band-top{position:absolute;left:0;top:0;width:100%;height:95px;background:var(--orange-light)}
  .title-band-bottom{position:absolute;left:0;top:95px;width:100%;height:55px;background:var(--orange-dark)}
  .title{position:absolute;left:16px;font-family:'Montserrat',sans-serif;font-weight:800;color:var(--white);font-size:54px;line-height:1;letter-spacing:-2px}
  .title-line-1{top:48px}
  .title-line-2{top:99px}
  .photo{position:absolute;left:0;top:156px;width:100%;height:183px;background:linear-gradient(100deg,#d9c7b3 0%,#efe7de 35%,#f3c0bd 60%,#f7f4f0 85%,#e9efe6 100%)}
  .services{position:absolute;left:32px;top:356px}
  .services-heading{font-family:'Barlow Semi Condensed',sans-serif;font-weight:600;color:var(--orange-text);font-size:20px;line-height:24px}
  .service-list{list-style:none;margin-top:1px}
  .service-list li{font-size:12px;line-height:16.2px;color:var(--text-grey);padding-left:10px;position:relative}
  .service-list li::before{content:"";position:absolute;left:1px;top:6.5px;width:3.5px;height:3.5px;border-radius:50%;background:var(--orange-text)}
  .service-list .note{display:block;font-size:7.6px;line-height:10px;margin-bottom:1px}
  .appointment-heading{position:absolute;left:33px;top:638px;font-family:'Barlow Semi Condensed',sans-serif;font-weight:600;color:var(--orange-text);font-size:11.5px;line-height:14px;letter-spacing:.2px}
  .practice-mark{position:absolute;left:33px;top:664px;width:30px;height:30px;background:var(--navy)}
  .practice-name{position:absolute;left:74px;top:664px;font-size:11.5px;line-height:13px;font-weight:600;color:var(--navy);text-transform:uppercase}
  .practice-address{position:absolute;left:74px;top:697px;font-size:9.6px;line-height:12px;color:var(--text-grey)}
  .member-badge{position:absolute;left:208px;top:666px;width:40px;height:34px;border-radius:50%;background:var(--badge-blue)}
  .footer-waves{position:absolute;left:0;top:705px;width:352px;height:155px;display:block}
  .website{position:absolute;left:32px;top:764px;font-size:9.6px;line-height:12px;font-weight:600;color:var(--white)}
</style>
</head>
<body>
  <main class="banner">
    <div class="title-band-top"></div>
    <div class="title-band-bottom"></div>
    <h1>
      <span class="title title-line-1">PHYSIO-</span>
      <span class="title title-line-2">THERAPY</span>
    </h1>

    <div class="photo" role="img" aria-label="Photo of a physiotherapist guiding an older woman through a resistance band exercise in a bright clinic"></div>

    <section class="services">
      <h2 class="services-heading">SERVICES</h2>
      <ul class="service-list">
        <li>Arthritis</li>
        <li>Back pain / Neck pain</li>
        <li>Sciatic pain</li>
        <li>Sports injuries</li>
        <li>Repetitive strain injuries</li>
        <li>Post surgical management<span class="note">(hip and knee arthroscopes, joint replacement surgery)</span></li>
        <li>Shoulder pain and dysfunction</li>
        <li>Tennis elbow</li>
        <li>Postural pain</li>
        <li>Workplace injuries</li>
        <li>Motor vehicle accidents</li>
        <li>Women’s health issues</li>
        <li>Clinical exercise</li>
        <li>Pre-employment functional assessments</li>
      </ul>
    </section>

    <h3 class="appointment-heading">MAKE AN APPOINTMENT</h3>
    <div class="practice-mark"></div>
    <p class="practice-name">Maplewood<br>Family Practice</p>
    <p class="practice-address">18-20 Linden Rd<br>Maplewood VIC 3190<br>(03) 9555 0142</p>
    <div class="member-badge" aria-label="Professional association member badge"></div>

    <svg class="footer-waves" viewBox="0 0 352 155" aria-hidden="true">
      <path d="M0,105 Q170,70 352,33 L352,155 L0,155 Z" fill="var(--orange-light)"/>
      <path d="M0,50 Q180,45 352,7 L352,33 Q170,70 0,105 Z" fill="var(--orange-dark)"/>
      <path d="M132,155 Q260,90 352,45 L352,155 Z" fill="var(--pale)"/>
    </svg>
    <p class="website">www.maplewoodfamilypractice.com.au</p>
  </main>
</body>
</html>
```